Company's name is: Merry Harvest Foods, Inc.; Product is: Smoked Chicken

Need a high quality, attractive, colorful label that will be used on our smoked chicken packaging. Our packaging consists of a regular plastic tray for whole chicken, with a clear bumpy cover that snaps over the tray. The label will be placed on top of the clear cover.
We are looking for a unique label. This could feature a nice picture of a whole golden brown smoked chicken, the company's name and address (or its initials MHF) nicely scripted, the nutrition panel, the name of the product it contains "Smoked Chicken - Cooked", weight, etc.
Please note that smoked chicken will be distributed to supermarkets, restaurants and health food stores.
We are thinking that the label should include nice colors (maybe a mixture of blue, red, golden brown, etc?) that will make our product catchy to the eyes and stand out on the shelves. We will have 2 varieties of smoked chicken: Fresh AND Organic.

Target Market(s)

Supermarkets
Wholesale delivery to restaurants
Valmart
TK's

Industry/Entity Type

It Company

Font styles to use
Decorative
Script

Requirements
Must have
• A nice picture of golden brown smoked chicken.
• Creative colors (~3) on the label
• Different sizes and fonts
• the company's name and address (or its initials MHF) nicely scripted, the nutrition panel, the name of the product it contains "Smoked Chicken - Cooked", weight, etc.
Nice to have
• There are some nice labels on Smoked chicken sold in Europe (France, Germany, etc). We suggest using Searchly to see some for inspiration if necessary.
Should not have
• My project must not be crowded with writings. A clean, attractive and professionally designed label is what we are looking for.
• Picture of the whole smoked chicken should be as natural looking as possible.

```html
<!DOCTYPE html>
<html lang="en">
<head>
<meta charset="utf-8">
<title>MHF's Smoked Chicken Labels</title>
<link rel="stylesheet" href="https://fonts.googleapis.com/css2?family=Audiowide&family=Kalam:wght@400&family=Open+Sans:wght@400&display=swap">
<style>
  :root {
    --page: #ffffff;
    --white: #ffffff;
    --cooked-red: #8c1b1e;
    --sky-top: #ff2e12;
    --sky-mid: #ff6a14;
    --sky-low: #ff9a1e;
    --roast-dark: #5a2410;
    --roast-light: #b5652c;
    --board: #8a5a2e;
    --greens: #4f8f2a;
    --fresh-band: #0b1c8e;
    --fresh-panel-a: #0a1786;
    --fresh-panel-b: #1d3fe2;
    --organic-band: #1e9a29;
    --organic-panel-a: #1a8427;
    --organic-panel-b: #3fe24d;
  }
  * { margin: 0; padding: 0; box-sizing: border-box; }
  html, body { width: 1200px; height: 960px; overflow: hidden; background: var(--page); }
  .sheet {
    width: 1200px; height: 960px;
    display: flex; justify-content: center; align-items: center; gap: 40px;
  }
  .label { width: 546px; height: 791px; display: block; }
  .label--fresh { --band: var(--fresh-band); --panel-a: var(--fresh-panel-a); --panel-b: var(--fresh-panel-b); }
  .label--organic { --band: var(--organic-band); --panel-a: var(--organic-panel-a); --panel-b: var(--organic-panel-b); }
  .band { fill: var(--band); }
  .panel-stop-a { stop-color: var(--panel-a); }
  .panel-stop-b { stop-color: var(--panel-b); }
  .brand { font-family: "Audiowide", sans-serif; font-size: 40px; fill: var(--white); }
  .product-name { font-family: "Audiowide", sans-serif; font-size: 37px; fill: var(--white); }
  .cooked-box { fill: var(--cooked-red); }
  .cooked { font-family: "Audiowide", sans-serif; font-size: 22px; fill: var(--white); }
  .variety { font-family: "Kalam", cursive; font-size: 44px; fill: var(--white); }
  .weight { font-family: "Audiowide", sans-serif; font-size: 17px; fill: var(--white); letter-spacing: 0.5px; }
  .body-copy, .maker { font-family: "Open Sans", sans-serif; font-size: 9.6px; fill: var(--white); }
  .nutrition-frame { fill: none; stroke: var(--white); stroke-width: 3; }
  .nutrition-rule { stroke: var(--white); stroke-width: 0.8; }
  .nutrition-head { font-family: "Open Sans", sans-serif; font-size: 7.5px; fill: var(--white); }
</style>
</head>
<body>
<main class="sheet">

  <svg class="label label--fresh" viewBox="0 0 390 565" role="group" aria-label="Fresh smoked chicken label">
    <defs>
      <linearGradient id="panel-fresh" x1="0" y1="0" x2="1" y2="1">
        <stop offset="0" class="panel-stop-a"/><stop offset="1" class="panel-stop-b"/>
      </linearGradient>
      <linearGradient id="sky-fresh" x1="0" y1="0" x2="0" y2="1">
        <stop offset="0" stop-color="var(--sky-top)"/><stop offset="0.45" stop-color="var(--sky-mid)"/><stop offset="1" stop-color="var(--sky-low)"/>
      </linearGradient>
      <linearGradient id="roast-fresh" x1="0" y1="0" x2="1" y2="0">
        <stop offset="0" stop-color="var(--roast-dark)"/><stop offset="0.5" stop-color="var(--roast-light)"/><stop offset="1" stop-color="var(--roast-dark)"/>
      </linearGradient>
      <linearGradient id="plate-fresh" x1="0" y1="0" x2="1" y2="0">
        <stop offset="0" stop-color="var(--roast-light)"/><stop offset="0.45" stop-color="var(--board)"/><stop offset="0.8" stop-color="var(--greens)"/><stop offset="1" stop-color="var(--roast-dark)"/>
      </linearGradient>
      <clipPath id="disc-fresh"><circle cx="195" cy="192" r="192"/></clipPath>
    </defs>
    <rect x="35" y="300" width="318" height="262" fill="url(#panel-fresh)"/>
    <g clip-path="url(#disc-fresh)">
      <rect x="0" y="0" width="390" height="165" fill="url(#sky-fresh)" role="img" aria-label="Orange sky behind grilled smoked chicken"/>
      <path d="M0 110 Q120 55 250 80 Q330 95 390 120 L390 165 L0 165 Z" fill="url(#roast-fresh)" role="img" aria-label="Golden brown smoked chicken skin"/>
      <rect x="0" y="228" width="390" height="160" fill="url(#plate-fresh)" role="img" aria-label="Carved chicken on a wooden board with fresh greens"/>
    </g>
    <text class="brand" x="195" y="145" text-anchor="middle">MHF's</text>
    <rect class="band" x="0" y="162" width="390" height="68"/>
    <text class="product-name" x="195" y="210" text-anchor="middle">SMOKED CHICKEN</text>
    <rect class="cooked-box" x="140" y="232" width="110" height="43"/>
    <text class="cooked" x="195" y="261" text-anchor="middle">COOKED</text>
    <text class="variety" x="188" y="326" text-anchor="middle">Fresh</text>
    <text class="weight" x="188" y="362" text-anchor="middle">weight - 1kg</text>
    <text class="body-copy" x="45" y="401" textLength="196" lengthAdjust="spacing">Lorem Ipsum is simply dummy text of the</text>
    <text class="body-copy" x="45" y="418" textLength="196" lengthAdjust="spacing">printing and typesetting industry. Lorem</text>
    <text class="body-copy" x="45" y="435" textLength="196" lengthAdjust="spacing">Ipsum has been the industry's standard</text>
    <text class="body-copy" x="45" y="452" textLength="196" lengthAdjust="spacing">dummy text ever since the 1500s, when an</text>
    <text class="body-copy" x="45" y="469">unknown printer took a galley of type and</text>
    <text class="maker" x="45" y="505">Manufatured By - Merry Harvest Foods, Inc.</text>
    <text class="maker" x="155" y="522" text-anchor="middle">123, street name,</text>
    <text class="maker" x="155" y="539" text-anchor="middle">Country name</text>
    <rect class="nutrition-frame" x="252" y="396" width="93" height="127"/>
    <line class="nutrition-rule" x1="299" y1="399" x2="299" y2="520"/>
    <text class="nutrition-head" x="258" y="411">Nutrition</text>
    <text class="nutrition-head" x="306" y="411">Per kg</text>
  </svg>

  <svg class="label label--organic" viewBox="0 0 390 565" role="group" aria-label="Organic smoked chicken label">
    <defs>
      <linearGradient id="panel-organic" x1="0" y1="0" x2="1" y2="1">
        <stop offset="0" class="panel-stop-a"/><stop offset="1" class="panel-stop-b"/>
      </linearGradient>
      <linearGradient id="sky-organic" x1="0" y1="0" x2="0" y2="1">
        <stop offset="0" stop-color="var(--sky-top)"/><stop offset="0.45" stop-color="var(--sky-mid)"/><stop offset="1" stop-color="var(--sky-low)"/>
      </linearGradient>
      <linearGradient id="roast-organic" x1="0" y1="0" x2="1" y2="0">
        <stop offset="0" stop-color="var(--roast-dark)"/><stop offset="0.5" stop-color="var(--roast-light)"/><stop offset="1" stop-color="var(--roast-dark)"/>
      </linearGradient>
      <linearGradient id="plate-organic" x1="0" y1="0" x2="1" y2="0">
        <stop offset="0" stop-color="var(--roast-light)"/><stop offset="0.45" stop-color="var(--board)"/><stop offset="0.8" stop-color="var(--greens)"/><stop offset="1" stop-color="var(--roast-dark)"/>
      </linearGradient>
      <clipPath id="disc-organic"><circle cx="195" cy="192" r="192"/></clipPath>
    </defs>
    <rect x="35" y="300" width="318" height="262" fill="url(#panel-organic)"/>
    <g clip-path="url(#disc-organic)">
      <rect x="0" y="0" width="390" height="165" fill="url(#sky-organic)" role="img" aria-label="Orange sky behind grilled smoked chicken"/>
      <path d="M0 110 Q120 55 250 80 Q330 95 390 120 L390 165 L0 165 Z" fill="url(#roast-organic)" role="img" aria-label="Golden brown smoked chicken skin"/>
      <rect x="0" y="228" width="390" height="160" fill="url(#plate-organic)" role="img" aria-label="Carved chicken on a wooden board with fresh greens"/>
    </g>
    <text class="brand" x="195" y="145" text-anchor="middle">MHF's</text>
    <rect class="band" x="0" y="162" width="390" height="68"/>
    <text class="product-name" x="195" y="210" text-anchor="middle">SMOKED CHICKEN</text>
    <rect class="cooked-box" x="140" y="232" width="110" height="43"/>
    <text class="cooked" x="195" y="261" text-anchor="middle">COOKED</text>
    <text class="variety" x="188" y="326" text-anchor="middle">Organic</text>
    <text class="weight" x="188" y="362" text-anchor="middle">weight - 1kg</text>
    <text class="body-copy" x="45" y="401" textLength="196" lengthAdjust="spacing">Lorem Ipsum is simply dummy text of the</text>
    <text class="body-copy" x="45" y="418" textLength="196" lengthAdjust="spacing">printing and typesetting industry. Lorem</text>
    <text class="body-copy" x="45" y="435" textLength="196" lengthAdjust="spacing">Ipsum has been the industry's standard</text>
    <text class="body-copy" x="45" y="452" textLength="196" lengthAdjust="spacing">dummy text ever since the 1500s, when an</text>
    <text class="body-copy" x="45" y="469">unknown printer took a galley of type and</text>
    <text class="maker" x="45" y="505">Manufatured By - Merry Harvest Foods, Inc.</text>
    <text class="maker" x="155" y="522" text-anchor="middle">123, street name,</text>
    <text class="maker" x="155" y="539" text-anchor="middle">Country name</text>
    <rect class="nutrition-frame" x="252" y="396" width="93" height="127"/>
    <line class="nutrition-rule" x1="299" y1="399" x2="299" y2="520"/>
    <text class="nutrition-head" x="258" y="411">Nutrition</text>
    <text class="nutrition-head" x="306" y="411">Per kg</text>
  </svg>

</main>
</body>
</html>
```